Evertide Planting Works and Tender-Shoot Emporium

The billboard will be on highway frontage and located directly next to my business building the marketing is for. The marketing on the billboard will be more directed towards the micro-greens superstore service being provided. And since the sign is on the businesses property it will need to say, "Exit Right Now" along with an arrow pointing to the right when facing the sign.

```html
<!DOCTYPE html>
<html lang="en">
<head>
<meta charset="utf-8">
<title>Evertide Planting Works – Exit Right Now Billboard</title>
<link rel="stylesheet" href="https://fonts.googleapis.com/css2?family=Montserrat:wght@700;900&display=swap">
<style>
  :root {
    --board-black: #111214;
    --divider-white: #ffffff;
    --arrow-green: #5aa331;
    --arrow-green-deep: #3f8a22;
    --headline-white: #ffffff;
    --headline-shadow: #1f4a12;
    --brand-green: #8cc63f;
    --grass-dark: #2f4a1c;
    --wood-brown: #4a3322;
    --plate-dark: #1b1b1d;
  }
  html, body {
    margin: 0;
    padding: 0;
    width: 1200px;
    height: 478px;
    overflow: hidden;
    background: var(--board-black);
  }
  .billboard {
    position: relative;
    width: 1200px;
    height: 478px;
    overflow: hidden;
  }
  .billboard-art {
    display: block;
    width: 1200px;
    height: 478px;
  }
  .brand-name {
    font-family: "Montserrat", Arial, sans-serif;
    font-weight: 700;
    fill: var(--brand-green);
  }
  .headline {
    font-family: "Montserrat", Arial, sans-serif;
    font-weight: 900;
    fill: var(--headline-white);
  }
</style>
</head>
<body>
<main class="billboard">
  <svg class="billboard-art" viewBox="0 0 1200 478" xmlns="http://www.w3.org/2000/svg">
    <defs>
      <linearGradient id="sprout-strip" x1="0" y1="0" x2="1" y2="1">
        <stop offset="0" stop-color="#3d2a1c"/>
        <stop offset="0.5" stop-color="#2f4a1c"/>
        <stop offset="1" stop-color="#5c7a2e"/>
      </linearGradient>
      <linearGradient id="arrow-fill" x1="0" y1="0" x2="1" y2="1">
        <stop offset="0" stop-color="#5aa331"/>
        <stop offset="1" stop-color="#3f8a22"/>
      </linearGradient>
      <radialGradient id="microgreen-bowl" cx="0.5" cy="0.45" r="0.6">
        <stop offset="0" stop-color="#7a2f55"/>
        <stop offset="0.5" stop-color="#2a2a2c"/>
        <stop offset="1" stop-color="#121213"/>
      </radialGradient>
      <linearGradient id="burger-plate" x1="0" y1="0" x2="1" y2="1">
        <stop offset="0" stop-color="#3a2618"/>
        <stop offset="0.6" stop-color="#7a5234"/>
        <stop offset="1" stop-color="#b9b4ae"/>
      </linearGradient>
      <radialGradient id="salad-plate" cx="0.45" cy="0.55" r="0.6">
        <stop offset="0" stop-color="#c9772a"/>
        <stop offset="0.45" stop-color="#3d5a26"/>
        <stop offset="1" stop-color="#1b1b1d"/>
      </radialGradient>
      <linearGradient id="juice-board" x1="0" y1="0" x2="1" y2="1">
        <stop offset="0" stop-color="#d8d0c0"/>
        <stop offset="0.35" stop-color="#2f7a2a"/>
        <stop offset="1" stop-color="#4a3322"/>
      </linearGradient>
      <filter id="headline-drop" x="-10%" y="-10%" width="130%" height="130%">
        <feDropShadow dx="4" dy="4" stdDeviation="0" flood-color="#1f4a12" flood-opacity="1"/>
      </filter>
    </defs>

    <rect class="board-backdrop" x="0" y="0" width="1200" height="478" fill="var(--board-black)"/>

    <g role="img" aria-label="Photo of sprouting micro-green seedlings on a dark wooden board">
      <rect class="sprout-strip" x="290" y="0" width="456" height="478" fill="url(#sprout-strip)"/>
    </g>

    <polygon class="arrow-outline" points="278,0 629,0 732,239 629,478 278,478 375,239" fill="var(--divider-white)"/>
    <polygon class="arrow-body" points="290,0 617,0 718,239 617,478 290,478 387,239" fill="url(#arrow-fill)" opacity="0.96"/>
    <polygon class="black-panel" points="0,0 278,0 375,239 278,478 0,478" fill="var(--board-black)"/>

    <rect class="grid-gutter" x="744" y="0" width="456" height="478" fill="var(--divider-white)"/>

    <g role="img" aria-label="Photo of pink-stemmed radish micro-greens in a dark bowl">
      <rect x="748" y="0" width="170" height="232" fill="url(#microgreen-bowl)"/>
    </g>
    <g role="img" aria-label="Photo of a burger topped with micro-greens on a plate on a wooden table">
      <rect x="926" y="0" width="274" height="232" fill="url(#burger-plate)"/>
    </g>
    <g role="img" aria-label="Photo of a salad with pumpkin, mozzarella and micro-greens on a black plate">
      <rect x="748" y="240" width="274" height="238" fill="url(#salad-plate)"/>
    </g>
    <g role="img" aria-label="Photo of a glass of green wheatgrass juice on a wooden board">
      <rect x="1030" y="240" width="170" height="238" fill="url(#juice-board)"/>
    </g>

    <text class="brand-name" aria-label="Evertide Planting Works and Tender-Shoot Emporium">
      <tspan x="28" y="192" font-size="56" textLength="272" lengthAdjust="spacingAndGlyphs">Evertide</tspan>
      <tspan x="28" y="240" font-size="38" textLength="272" lengthAdjust="spacingAndGlyphs">Planting Works</tspan>
      <tspan x="28" y="276" font-size="18" textLength="272" lengthAdjust="spacingAndGlyphs">and Tender-Shoot Emporium</tspan>
    </text>

    <g class="headline" filter="url(#headline-drop)">
      <text x="394" y="189" font-size="150" textLength="240" lengthAdjust="spacingAndGlyphs">EXIT</text>
      <text x="394" y="286" font-size="114" textLength="240" lengthAdjust="spacingAndGlyphs">RIGHT</text>
      <text x="394" y="394" font-size="133" textLength="236" lengthAdjust="spacingAndGlyphs">NOW</text>
    </g>
  </svg>
</main>
</body>
</html>
```